IT Security Company Website

We would like to create a new look for our current company site veltrom.io. The company offercyber security services for banks, goverment etc. Therefore a very professional look is important. We need at least 2 pages designed.

Target Market(s)

B2B

Coding

Coded - Design and coding required

Number of Pages Required

1 page

```html
<!DOCTYPE html>
<html lang="en">
<head>
<meta charset="utf-8">
<title>Veltrom — Defend Against Cyber-Attacks</title>
<link href="https://fonts.googleapis.com/css2?family=Poppins:wght@300;400;500;600;700&display=swap" rel="stylesheet">
<style>
:root{
  --navy:#0f1a3f;
  --navy-deep:#0b1433;
  --card:#1c2a55;
  --gold:#edc546;
  --gold-soft:#f3d36a;
  --ink:#111522;
  --light:#eeeff1;
  --white:#ffffff;
}
*{margin:0;padding:0;box-sizing:border-box}
html,body{width:1200px;height:2843px;overflow:hidden}
body{font-family:'Poppins',sans-serif;background:var(--navy);color:var(--white);position:relative}
.abs{position:absolute}
.btn{position:absolute;display:flex;align-items:center;justify-content:center;background:var(--gold);color:var(--ink);font-weight:600;font-size:12px;border-radius:24px;text-decoration:none}

/* hero */
.hero{position:absolute;left:0;top:0;width:1200px;height:695px;background:radial-gradient(ellipse at 20% 40%,#27345e 0%,var(--navy) 60%,var(--navy-deep) 100%)}
.logo{font-weight:300;font-size:44px;letter-spacing:2px;color:var(--white);line-height:1}
.nav a{position:absolute;top:62px;font-size:12px;color:var(--white);text-decoration:none}
.nav a.active{color:var(--gold);font-weight:600}
.welcome{left:211px;top:228px;font-size:15px;letter-spacing:10px;font-weight:400}
.welcome b{color:var(--gold);font-weight:700}
.hero h1{position:absolute;left:210px;top:264px;font-size:48px;line-height:57px;font-weight:600}
.hero h1 span{color:var(--gold);font-weight:700}
.hero p{left:211px;top:390px;width:420px;font-size:12.5px;line-height:21px}
.hero-art{left:690px;top:140px;width:440px;height:470px;border-radius:50%;background:radial-gradient(circle at 50% 45%,rgba(243,211,106,.55) 0%,rgba(237,197,70,.2) 35%,rgba(15,26,63,0) 68%)}

/* intro */
.intro{position:absolute;left:0;top:695px;width:1200px;height:481px;background:linear-gradient(120deg,#fafafa 0%,var(--light) 55%,#e2e3e7 100%);color:var(--ink)}
.intro-art{left:222px;top:65px;width:380px;height:350px;border-radius:14px;background:linear-gradient(160deg,#f4f4f5 0%,#e7dfbf 55%,#2b2f3a 100%)}
.intro-rule{left:630px;top:88px;width:345px;height:3px;background:var(--gold)}
.intro h2{position:absolute;left:630px;top:122px;font-size:32px;line-height:36px;font-weight:600}
.intro p{left:630px;width:380px;font-size:12.5px;line-height:21.5px}

/* risks */
.risks{position:absolute;left:0;top:1176px;width:1200px;height:918px;background:radial-gradient(ellipse at 50% 45%,#1b2852 0%,var(--navy) 65%)}
.risks h2{position:absolute;left:0;width:1200px;top:60px;text-align:center;font-size:30px;font-weight:700}
.risk-card{position:absolute;width:237px;height:239px;background:rgba(44,58,104,.55);border:1px solid rgba(120,140,200,.35);border-radius:10px;text-align:center;padding:68px 18px 0}
.risk-card .badge{position:absolute;left:68px;top:-52px;width:100px;height:100px;border-radius:50%;background:var(--gold);border:5px solid var(--white);box-shadow:0 0 24px rgba(237,197,70,.7)}
.risk-card h3{font-size:19px;line-height:21px;font-weight:600;margin-bottom:8px}
.risk-card p{font-size:12px;line-height:21.5px;font-weight:500;color:#d6dbea}

/* signup */
.signup{position:absolute;left:0;top:2094px;width:1200px;height:399px;background:linear-gradient(90deg,#f4f4f6 0%,#e9eaee 60%,#e2e4ea 100%);color:var(--ink)}
.signup h2{position:absolute;left:210px;top:150px;font-size:30px;line-height:36px;font-weight:700}
.signup-art{left:790px;top:86px;width:210px;height:220px;background:radial-gradient(circle,rgba(237,197,70,.85) 0%,rgba(237,197,70,.35) 45%,rgba(237,197,70,0) 70%)}

/* footer */
.footer{position:absolute;left:0;top:2493px;width:1200px;height:304px;background:var(--navy)}
.footer p.about{left:210px;top:122px;width:230px;font-size:12.5px;line-height:21.5px}
.footer h4{position:absolute;top:83px;font-size:14px;font-weight:600;color:var(--gold)}
.footer ul{position:absolute;top:113px;list-style:none;font-size:12.5px}
.footer li{height:28px}
.contact-item{position:absolute;left:821px;display:flex;align-items:center;gap:14px;font-size:12px;line-height:14px}
.contact-item .ico{width:27px;height:27px;border-radius:50%;background:var(--gold);display:flex;align-items:center;justify-content:center}
.copyright{position:absolute;left:0;top:2797px;width:1200px;height:46px;background:var(--gold);display:flex;align-items:center;justify-content:center;font-size:12px;font-weight:500;color:var(--white)}
</style>
</head>
<body>

<section class="hero">
  <div class="abs logo" style="left:209px;top:50px">VELTROM</div>
  <nav class="nav">
    <a class="active" href="#" style="left:451px">Home</a>
    <a href="#" style="left:519px">Q&amp;A</a>
    <a href="#" style="left:577px">Pricing</a>
    <a href="#" style="left:650px">About us</a>
    <a href="#" style="left:735px">Resources</a>
  </nav>
  <a class="btn" href="#" style="left:850px;top:48px;width:140px;height:45px">CONTACT US</a>

  <div class="abs welcome">WELCOME TO <b>VELTROM</b></div>
  <h1>DEFEND AGAINST<br><span>CYBER-ATTACKS</span></h1>
  <p class="abs">Lorem ipsum dolor sit amet, consectetur adipiscing elit, sed do eiusmod tempor incididunt ut labore et dolore magna aliqua.</p>
  <a class="btn" href="#" style="left:211px;top:460px;width:141px;height:45px">GET STARTED</a>
  <div class="abs hero-art" role="img" aria-label="Golden shield with a tick, circled by a light ring and small floating gear icons"></div>
</section>

<section class="intro">
  <div class="abs intro-art" role="img" aria-label="Illustration of a laptop with a padlocked shield, surrounded by card, mail, chat, folder, cart and globe icons"></div>
  <div class="abs intro-rule"></div>
  <h2>The CISO’s Solution –<br>forewarned is forearmed.</h2>
  <p class="abs" style="top:208px">Veltrom helps you understand when, where and how stolen or accidentally leaked information is exposed. Veltrom’s alerting service can also detect threats before they turn into incidents. There are certain indicators that can be measured.</p>
  <p class="abs" style="top:315px">Before an attack takes place, hackers often reserve similar domain names (typosquatting), they spoof profiles in social media like ProLink or they exchange information about targets in hacker forums.</p>
</section>

<section class="risks">
  <h2>WHAT RISKS CAN BE MITIGATED WITH VELTROM?</h2>

  <div class="risk-card" style="left:225px;top:191px">
    <div class="badge" role="img" aria-label="Phishing icon"></div>
    <h3>Prevent phishing</h3>
    <p>We monitor all new domain registrations (ccTLDs, gTLDs, uTLD, sTLD). In doing so, we also record typical typosquatting techniques. Veltrom utomatically analyzes domains</p>
  </div>
  <div class="risk-card" style="left:482px;top:191px">
    <div class="badge" role="img" aria-label="Server and cloud icon"></div>
    <h3>Detect exposed infrastructure</h3>
    <p>We monitor server access, IOT (Scanhub) or complete DB dumps in different formats (CSV, Memory Dumps, Office Files etc).</p>
  </div>
  <div class="risk-card" style="left:738px;top:191px">
    <div class="badge" role="img" aria-label="Data leak icon"></div>
    <h3>Detect leaks from ransomware</h3>
    <p>In ransomware attacks, victims are blackmailed into paying a ransom sum in order to regain access to their own data. In some cases, ransoms are not</p>
  </div>

  <div class="risk-card" style="left:225px;top:513px">
    <div class="badge" role="img" aria-label="Hooded figure at a laptop icon"></div>
    <h3>Find exposed data in the darknet</h3>
    <p>Monitoring whether your organisation’s name appears in Dark Web forums, Onion-, I2P and paste sites can help you detect potential insider threats,</p>
  </div>
  <div class="risk-card" style="left:482px;top:513px">
    <div class="badge" role="img" aria-label="Spoofed email icon"></div>
    <h3>Detect spoofing and impersonation</h3>
    <p>We monitor social media services such as Chirper, Threadly, Vidstream, Wiremsg, etc. for posts that could be damaging to our reputation.</p>
  </div>
  <div class="risk-card" style="left:738px;top:513px">
    <div class="badge" role="img" aria-label="Group of employees icon"></div>
    <h3>Understand employee exposure</h3>
    <p>Employees who are heavily exposed to the Internet are at greater risk of social engineering attacks such as phishing.</p>
  </div>

  <a class="btn" href="#" style="left:516px;top:806px;width:167px;height:45px">VIEW ALL SERVICES</a>
</section>

<section class="signup">
  <h2>SIGN UP FOR CYBER<br>THREAT INTELLIGENCE ALERTS</h2>
  <a class="btn" href="#" style="left:210px;top:235px;width:146px;height:44px">SIGN UP NOW</a>
  <div class="abs signup-art" role="img" aria-label="Three yellow warning triangles with exclamation marks"></div>
</section>

<footer class="footer">
  <div class="abs logo" style="left:209px;top:66px">VELTROM</div>
  <p class="abs about">Lorem ipsum dolor sit amet, consectetur adipiscing elit, sed do eiusmod tempor incididunt ut labore et dolore magna aliqua. Quis ipsum suspendisse ultrices gravida.</p>

  <h4 style="left:515px">Quicks Links</h4>
  <ul style="left:515px"><li>Home</li><li>Q&amp;A</li><li>Pricing</li><li>About us</li><li>Contact</li><li>Resources</li></ul>

  <h4 style="left:657px">Resources</h4>
  <ul style="left:657px"><li>Lorem ipsum</li><li>dolor sit</li><li>amet,</li><li>consectetur</li><li>adipiscing</li></ul>

  <h4 style="left:821px">Contact Us</h4>
  <div class="contact-item" style="top:112px">
    <span class="ico"><svg width="12" height="14" viewBox="0 0 12 14"><path d="M6 0a5 5 0 0 0-5 5c0 4 5 9 5 9s5-5 5-9a5 5 0 0 0-5-5zm0 7a2 2 0 1 1 0-4 2 2 0 0 1 0 4z" fill="#fff"/></svg></span>
    <span>0000 somewhere st.<br>000 somewhere</span>
  </div>
  <div class="contact-item" style="top:162px">
    <span class="ico"><svg width="13" height="13" viewBox="0 0 24 24"><path d="M6.6 10.8a15 15 0 0 0 6.6 6.6l2.2-2.2c.3-.3.7-.4 1-.2 1.1.4 2.3.6 3.6.6.6 0 1 .4 1 1V20c0 .6-.4 1-1 1A17 17 0 0 1 3 4c0-.6.4-1 1-1h3.5c.6 0 1 .4 1 1 0 1.3.2 2.5.6 3.6.1.3 0 .7-.2 1l-2.3 2.2z" fill="#fff"/></svg></span>
    <span>(012) 3456 7890</span>
  </div>
</footer>

<div class="copyright">COPYRIGHT © VELTROM ALL RIGHTS RESERVED.</div>

</body>
</html>
```